R & T Summit Construction Business Card ideas

We want a business card to represents our company in a way that looks professional but is also a business card that is unique!

Industry/Entity Type

Construction Company

Contact Information for Business Card

open to all design ideas, just want to be able to see different options to choose from in either color or grayscale.

Requirements
Must have
• Our names and phone numbers
• Nolan Pritchett 512-804-2271
• Curtis Hale 512-693-1804
• Business logo

```html
<!DOCTYPE html>
<html lang="en">
<head>
<meta charset="utf-8">
<title>R &amp; T Summit Construction – Business Card</title>
<link rel="stylesheet" href="https://fonts.googleapis.com/css2?family=Libre+Baskerville:wght@400&display=swap">
<style>
  :root {
    --backdrop: #e9e6e1;
    --card: #ffffff;
    --ink: #111111;
    --band-dark: #0d0d0d;
    --band-grey: #9a9a9a;
    --rule: #555555;
  }
  * { box-sizing: border-box; margin: 0; padding: 0; }
  html, body {
    width: 1200px;
    height: 900px;
    overflow: hidden;
    background: var(--backdrop);
  }
  .canvas {
    width: 1200px;
    height: 900px;
    display: flex;
    align-items: center;
    justify-content: center;
  }
  .business-card {
    position: relative;
    width: 840px;
    height: 480px;
    background: var(--card);
    box-shadow: 0 10px 30px rgba(0,0,0,0.18);
    font-family: "Libre Baskerville", "Times New Roman", serif;
    color: var(--ink);
    overflow: hidden;
  }
  .edge-band {
    position: absolute;
    top: 0;
    bottom: 0;
    width: 34px;
    display: flex;
    flex-direction: column;
  }
  .edge-band--left { left: 0; }
  .edge-band--right { right: 0; }
  .edge-band .dark { background: var(--band-dark); }
  .edge-band .grey { background: var(--band-grey); }
  .edge-band--left .dark { flex: 0 0 55%; }
  .edge-band--left .grey { flex: 1; }
  .edge-band--right .grey { flex: 0 0 45%; }
  .edge-band--right .dark { flex: 1; }

  .brand {
    position: absolute;
    top: 120px;
    left: 0;
    right: 0;
    display: flex;
    flex-direction: column;
    align-items: center;
  }
  .brand-name {
    display: flex;
    align-items: center;
    gap: 18px;
    font-size: 38px;
    letter-spacing: 1px;
    color: var(--ink);
  }
  .brand-mark {
    width: 22px;
    height: 22px;
    background: var(--ink);
  }
  .brand-rule {
    margin-top: 16px;
    width: 520px;
    height: 2px;
    background: var(--ink);
  }

  .contacts {
    position: absolute;
    top: 300px;
    left: 0;
    right: 0;
    display: flex;
    justify-content: center;
    align-items: center;
    gap: 36px;
  }
  .contact {
    text-align: center;
    font-size: 24px;
    line-height: 1.4;
  }
  .contact .phone { font-size: 22px; }
  .contact-divider {
    width: 1px;
    height: 72px;
    background: var(--rule);
    transform: rotate(14deg);
  }
</style>
</head>
<body>
  <main class="canvas">
    <article class="business-card">
      <div class="edge-band edge-band--left"><span class="dark"></span><span class="grey"></span></div>
      <div class="edge-band edge-band--right"><span class="grey"></span><span class="dark"></span></div>

      <header class="brand">
        <div class="brand-name"><span class="brand-mark"></span>R &amp; T Summit Construction</div>
        <div class="brand-rule"></div>
      </header>

      <section class="contacts">
        <div class="contact">
          <div class="name">Curtis Hale</div>
          <div class="phone">512-693-1804</div>
        </div>
        <div class="contact-divider"></div>
        <div class="contact">
          <div class="name">Nolan Pritchett</div>
          <div class="phone">512-804-2271</div>
        </div>
      </section>
    </article>
  </main>
</body>
</html>
```